Welcome signage for KWT Software Consulting Company

I need Welcome signage for KWT Consulting company Office Window. We are a Computer software company that offers software Implementation and Training for our Customers windows size 1. 900mm high 750mm wide. size 2. 1000mm high 700 wide.
Please review our website for branding and ideas.
The poster needs to contain our logo, website www.kwtadvisory-example.net.au and ph number 1300 46 81 02 , and the strap line... Empowering businesses with software choice.
Updates

Hi I'm really keen to find the perfect design. I had decided on one however the designer was dismissed from the group by admin so here I go again. Please read the briefs already in the information and hopefully I am excited by new submissions when I arrive to work on Monday xxx Thanks heaps fellow Designers x

```html
<!DOCTYPE html>
<html lang="en">
<head>
<meta charset="utf-8">
<title>KWT Consulting – Window Signage</title>
<link rel="stylesheet" href="https://fonts.googleapis.com/css2?family=Open+Sans:wght@300;400;600&display=swap">
<style>
  :root {
    --page-bg: #d6d6d6;
    --sign-bg: #ffffff;
    --amber: #f6a800;
    --orange: #e8620a;
    --accent: #e45d0a;
    --ink: #1f1f1f;
    --logo-grey: #555a5e;
  }
  html, body {
    margin: 0;
    width: 1200px;
    height: 1200px;
    overflow: hidden;
    background: var(--page-bg);
    font-family: "Open Sans", Arial, sans-serif;
  }
  .canvas { position: relative; width: 1200px; height: 1200px; }

  /* Shared scale: 0.7 px per mm */
  .sign { position: absolute; background: var(--sign-bg); overflow: hidden; }
  .sign--900x750  { left: 67px;  top: 320px; width: 525px; height: 630px; }
  .sign--1000x700 { left: 642px; top: 250px; width: 490px; height: 700px; }

  .brand {
    position: absolute; left: 0; top: 0; width: 100%;
    display: flex; align-items: center; justify-content: center; gap: 14px;
  }
  .brand__dot { border-radius: 50%; background: var(--orange); width: 44px; height: 44px; }
  .brand__name { color: var(--logo-grey); font-weight: 600; letter-spacing: 1px; font-size: 42px; white-space: nowrap; }
  .sign--900x750 .brand  { height: 180px; }
  .sign--1000x700 .brand { height: 190px; }

  .strap {
    position: absolute; left: 0; width: 100%;
    background: linear-gradient(90deg, var(--amber) 0%, var(--orange) 72%, var(--orange) 100%);
  }
  .strap__text { position: absolute; margin: 0; color: #fff; font-weight: 600; letter-spacing: 0.3px; white-space: nowrap; }
  .sign--900x750 .strap        { top: 180px; height: 260px; }
  .sign--900x750 .strap__text  { left: 46px; top: 38px; font-size: 54px; line-height: 62px; }
  .sign--1000x700 .strap       { top: 190px; height: 280px; }
  .sign--1000x700 .strap__text { left: 42px; top: 50px; font-size: 50px; line-height: 60px; }

  .contact__bar { position: absolute; width: 5px; background: var(--accent); }
  .contact__phone { position: absolute; margin: 0; color: var(--accent); font-weight: 600; line-height: 1; white-space: nowrap; }
  .contact__web { position: absolute; margin: 0; color: var(--ink); font-weight: 300; line-height: 1; white-space: nowrap; }
  .contact__web .domain { color: var(--accent); }

  .sign--900x750 .contact__bar   { left: 46px; top: 488px; height: 92px; }
  .sign--900x750 .contact__phone { left: 70px; top: 480px; font-size: 52px; }
  .sign--900x750 .contact__web   { left: 70px; top: 550px; font-size: 28px; }

  .sign--1000x700 .contact__bar   { left: 42px; top: 526px; height: 92px; }
  .sign--1000x700 .contact__phone { left: 64px; top: 518px; font-size: 50px; }
  .sign--1000x700 .contact__web   { left: 64px; top: 588px; font-size: 26px; }
</style>
</head>
<body>
<main class="canvas">

  <section class="sign sign--900x750" aria-label="Window sign, 900 mm high by 750 mm wide">
    <div class="brand">
      <span class="brand__dot"></span>
      <span class="brand__name">KWT Consulting</span>
    </div>
    <div class="strap">
      <p class="strap__text">Empowering<br>businesses with<br>software choice</p>
    </div>
    <span class="contact__bar"></span>
    <p class="contact__phone">1300 46 81 02</p>
    <p class="contact__web">www.<span class="domain">kwtadvisory-example</span>.net.au</p>
  </section>

  <section class="sign sign--1000x700" aria-label="Window sign, 1000 mm high by 700 mm wide">
    <div class="brand">
      <span class="brand__dot"></span>
      <span class="brand__name">KWT Consulting</span>
    </div>
    <div class="strap">
      <p class="strap__text">Empowering<br>businesses with<br>software choice</p>
    </div>
    <span class="contact__bar"></span>
    <p class="contact__phone">1300 46 81 02</p>
    <p class="contact__web">www.<span class="domain">kwtadvisory-example</span>.net.au</p>
  </section>

</main>
</body>
</html>
```